Redesign of current website

Redesign - pmwdtinc.com

Coding

Coded - Design and coding required

Number of Pages Required

4 page

Colors

Designer to choose colors to be used in the design.

```html
<!DOCTYPE html>
<html lang="en">
<head>
<meta charset="utf-8">
<title>Summit Field Solutions Group</title>
<link href="https://fonts.googleapis.com/css2?family=Barlow:wght@400;500;600&family=Raleway:wght@500;600;700&display=swap" rel="stylesheet">
<style>
:root{
  --green:#1aa314;
  --green-bright:#22b51b;
  --ink:#333333;
  --text:#555555;
  --light:#f4f4f4;
  --dark:#2f2f2f;
  --footer:#262626;
  --white:#ffffff;
}
*{box-sizing:border-box;margin:0;padding:0}
html,body{width:1200px;height:3751px;overflow:hidden}
body{position:relative;font-family:"Barlow",sans-serif;color:var(--text);background:var(--white)}
.abs{position:absolute}

/* header */
.site-header{position:absolute;left:0;top:0;width:1200px;height:147px;background:var(--white);border-top:3px solid var(--green)}
.brand{position:absolute;left:112px;top:30px;width:200px;font-family:"Barlow",sans-serif;font-weight:600;font-size:22px;line-height:26px;color:var(--green);text-transform:uppercase}
.contact-pill{position:absolute;top:22px;display:flex;align-items:center;gap:10px;font-size:16px;font-weight:500;color:var(--green)}
.contact-pill .dot{width:50px;height:50px;border-radius:50%;background:var(--green);display:flex;align-items:center;justify-content:center}
.main-nav{position:absolute;top:104px;left:0;width:1200px;font-size:12.5px;font-weight:500;color:var(--ink)}
.main-nav a{position:absolute;text-decoration:none;color:inherit;white-space:nowrap}
.main-nav a.active{color:var(--green)}

/* hero */
.hero{position:absolute;left:0;top:147px;width:1200px;height:721px;overflow:hidden}
.hero-photo{position:absolute;inset:0;background:linear-gradient(100deg,#2b3133 0%,#59605f 30%,#3a4444 55%,#1f2628 100%)}
.hero-copy{position:absolute;left:527px;top:240px;width:560px;text-align:center;color:var(--white)}
.hero-copy h1{font-family:"Raleway",sans-serif;font-weight:600;font-size:40px;line-height:46px}
.hero-copy h2{font-family:"Raleway",sans-serif;font-weight:600;font-size:30px;line-height:40px;margin-top:8px}
.hero-copy p{font-size:17px;line-height:32px;margin-top:14px}
.btn-solid{display:inline-block;background:var(--green-bright);color:var(--white);font-family:"Raleway",sans-serif;font-weight:600;font-size:19px;border-radius:34px;text-decoration:none;text-align:center}
.hero .btn-solid{margin-top:26px;width:219px;height:66px;line-height:66px}
.dots{position:absolute;left:575px;top:680px;display:flex;gap:6px}
.dots span{width:12px;height:12px;border-radius:50%;background:var(--white)}
.dots span.on{background:var(--green-bright)}

/* about */
.about{position:absolute;left:0;top:868px;width:1200px;height:582px;background:var(--light);overflow:hidden}
.about-photo{position:absolute;left:450px;top:0;width:750px;height:582px;background:linear-gradient(90deg,rgba(244,244,244,1) 0%,#dfe6ec 18%,#9fb2c4 55%,#2e4f7a 100%)}
.about h2{position:absolute;left:112px;top:58px;font-family:"Raleway",sans-serif;font-weight:600;font-size:24px;line-height:39px;color:var(--green)}
.about p{position:absolute;left:112px;top:159px;width:423px;font-size:14px;line-height:27.5px;text-align:justify;color:var(--ink)}
.about .btn-solid{position:absolute;left:112px;top:464px;width:178px;height:61px;line-height:61px;font-size:16px;font-weight:500}

/* services */
.section-title{position:absolute;left:0;width:1200px;text-align:center;font-family:"Raleway",sans-serif;font-weight:500;font-size:26px;color:var(--ink)}
.rule{position:absolute;height:3px;width:70px;background:var(--green)}
.card{position:absolute;top:1620px;width:303px;height:355px;background:var(--white);box-shadow:0 2px 8px rgba(0,0,0,.14);text-align:center}
.card svg{margin-top:20px}
.card h3{font-family:"Raleway",sans-serif;font-weight:600;font-size:16px;color:var(--ink);margin-top:10px}
.card p{font-size:14px;line-height:26px;color:var(--text);margin:12px 35px 0}
.btn-outline{display:inline-block;border:2px solid var(--green);color:var(--green);font-family:"Raleway",sans-serif;font-weight:600;font-size:14px;border-radius:26px;width:130px;height:50px;line-height:46px;text-decoration:none;margin-top:22px}

/* surveillance */
.surveil{position:absolute;left:0;top:2060px;width:1200px;height:508px;background:var(--dark);overflow:hidden}
.surveil-photo{position:absolute;left:35px;top:150px;width:505px;height:170px;border-radius:30px;background:linear-gradient(90deg,#3a3a3a,#8a8a8a 45%,#5a5a5a);opacity:.9}
.surveil h2{position:absolute;left:662px;top:80px;font-family:"Raleway",sans-serif;font-weight:600;font-size:24px;color:var(--white)}
.surveil p{position:absolute;left:662px;top:148px;width:420px;font-size:14px;line-height:29px;text-align:justify;color:var(--white)}
.btn-ghost{position:absolute;left:662px;top:408px;width:166px;height:57px;line-height:53px;border:2px solid var(--white);border-radius:30px;color:var(--white);text-align:center;font-family:"Raleway",sans-serif;font-weight:600;font-size:15px;text-decoration:none}

/* overview */
.overview h2{position:absolute;left:112px;top:2657px;font-family:"Raleway",sans-serif;font-weight:500;font-size:26px;color:var(--ink)}
.overview p{position:absolute;left:112px;top:2742px;width:450px;font-size:13px;line-height:27.5px;text-align:justify;color:var(--ink)}
.overview-diagram{position:absolute;left:645px;top:2630px;width:380px;height:345px;border-radius:50%;background:radial-gradient(circle,#eef2f5 0%,#f8f9fa 60%,#ffffff 100%)}

/* partners */
.partners{position:absolute;left:0;top:3055px;width:1200px;height:290px;background:#f2f2f2}
.logo-box{position:absolute;top:125px;width:179px;height:100px;background:var(--white);border:1px solid #e4e4e4;display:flex;align-items:center;justify-content:center}
.logo-box span{width:110px;height:26px;border-radius:4px;background:#d0d0d0}

/* footer */
.site-footer{position:absolute;left:0;top:3345px;width:1200px;height:406px;background:var(--footer);color:#a8a8a8}
.footer-brand{position:absolute;left:112px;top:40px;width:240px;font-weight:600;font-size:24px;line-height:30px;color:var(--green);text-transform:uppercase;text-align:center}
.footer-about{position:absolute;left:112px;top:180px;width:270px;font-size:14px;line-height:26px}
.footer-col h4{position:absolute;top:38px;font-family:"Barlow",sans-serif;font-weight:500;font-size:20px;color:var(--white);letter-spacing:.5px}
.footer-list{position:absolute;font-size:14px;line-height:26.5px;list-style:none}
.contact-list{left:423px;top:82px;width:260px;color:#d8d8d8}
.links-list{left:745px;top:82px;line-height:38px}
.social{position:absolute;left:968px;display:flex;align-items:center;gap:12px}
.social .ring{width:34px;height:34px;border-radius:50%;background:var(--white)}
.social small{display:block;font-size:11px;color:#9a9a9a;line-height:12px}
.social b{font-weight:400;font-size:16px;color:#bdbdbd;line-height:18px}
.footer-rule{position:absolute;left:112px;top:353px;width:976px;height:1px;background:#3d3d3d}
.copyright{position:absolute;left:0;top:370px;width:1200px;text-align:center;font-size:13px;color:var(--white)}
</style>
</head>
<body>

<header class="site-header">
  <div class="brand">Summit Field Solutions Group</div>
  <div class="contact-pill" style="left:541px">
    <span class="dot"><svg width="18" height="14" viewBox="0 0 18 14"><rect x="1" y="1" width="16" height="12" rx="1.5" fill="none" stroke="#fff" stroke-width="2"/><path d="M1 2l8 6 8-6" fill="none" stroke="#fff" stroke-width="2"/></svg></span>
    EMAIL : contact@pmwdtinc.com
  </div>
  <div class="contact-pill" style="left:842px">
    <span class="dot"><svg width="18" height="18" viewBox="0 0 24 24"><path d="M6.6 10.8a15 15 0 006.6 6.6l2.2-2.2c.3-.3.7-.4 1-.2 1.1.4 2.3.6 3.6.6.6 0 1 .4 1 1V20c0 .6-.4 1-1 1C10.6 21 3 13.4 3 4c0-.6.4-1 1-1h3.5c.6 0 1 .4 1 1 0 1.3.2 2.5.6 3.6.1.3 0 .7-.2 1z" fill="#fff"/></svg></span>
    CALL US : (555) 013-4821
  </div>
  <nav class="main-nav">
    <a class="active" style="left:450px">HOME</a>
    <a style="left:540px">ABOUT US</a>
    <a style="left:657px">WHO ARE WE</a>
    <a style="left:792px">OUR PARTNERS &amp; CLIENTS</a>
    <a style="left:1010px">CONTACT US</a>
  </nav>
</header>

<section class="hero">
  <div class="hero-photo" role="img" aria-label="Dome security camera mounted outside a modern glass building"></div>
  <div class="hero-copy">
    <h1>SUMMIT FIELD</h1>
    <h2>SOLUTIONS GROUP</h2>
    <p>We are a Self-certified Small Disabled Veteran Owned Business head quartered in Ridgefield, Georgia, the Home of our Field Team.</p>
    <a class="btn-solid">READ MORE</a>
  </div>
  <div class="dots"><span></span><span class="on"></span><span></span></div>
</section>

<section class="about">
  <div class="about-photo" role="img" aria-label="Technician in a hard hat installing a security camera while using a radio"></div>
  <h2>SUMMIT FIELD<br>SOLUTIONS GROUP, LLC (SFSG, LLC)</h2>
  <p>We are a Self-certified Small Disabled Veteran Owned Business headquartered in Ridgefield, Georgia, the Home of our Field Team. We support our clients by supporting security, training and operational needs by using the experience gained through our military service in special operations and advance infantry tactics. Our company was established based upon the success of propelling other organizations to reach their full potential. Experience has also shown us that rewarding employee for their hard work, loyalty, and dedication will have a positive impact and influence on the overall company as a whole!</p>
  <a class="btn-solid">LEARN MORE</a>
</section>

<section class="services">
  <h2 class="section-title" style="top:1514px">SERVICES &amp; PRODUCTS</h2>
  <div class="rule" style="left:565px;top:1565px"></div>

  <article class="card" style="left:112px">
    <svg width="122" height="128" viewBox="0 0 122 128"><path d="M61 4L116 24V62c0 30-24 52-55 62C30 114 6 92 6 62V24z" fill="none" stroke="#1aa314" stroke-width="4"/><circle cx="61" cy="56" r="14" fill="none" stroke="#333" stroke-width="2.5"/><circle cx="61" cy="56" r="5" fill="none" stroke="#333" stroke-width="2.5"/></svg>
    <h3>TECHNICAL SERVICES</h3>
    <p>Surveillance camera installations, training and maintenance</p>
    <a class="btn-outline">READ MORE</a>
  </article>

  <article class="card" style="left:448px">
    <svg width="122" height="128" viewBox="0 0 122 128"><path d="M61 4L116 24V62c0 30-24 52-55 62C30 114 6 92 6 62V24z" fill="none" stroke="#1aa314" stroke-width="4"/><path d="M38 54L61 36 84 54M44 50v30h34V50" fill="none" stroke="#333" stroke-width="2.5"/><rect x="53" y="60" width="16" height="14" fill="none" stroke="#333" stroke-width="2.5"/></svg>
    <h3>LOGISTICAL SERVICES</h3>
    <p>Supply management systems to include inventory, accountability</p>
    <a class="btn-outline">READ MORE</a>
  </article>

  <article class="card" style="left:784px">
    <svg width="122" height="128" viewBox="0 0 122 128"><path d="M61 4L116 24V62c0 30-24 52-55 62C30 114 6 92 6 62V24z" fill="none" stroke="#1aa314" stroke-width="4"/><rect x="42" y="58" width="38" height="24" fill="none" stroke="#333" stroke-width="2.5"/><path d="M50 52l16-12v22z" fill="none" stroke="#333" stroke-width="2.5"/></svg>
    <h3>PRODUCT MARKETING</h3>
    <p>Research and procurement of camera systems, system software</p>
    <a class="btn-outline">READ MORE</a>
  </article>
</section>

<section class="surveil">
  <svg class="abs" style="left:0;top:0" width="1200" height="508" viewBox="0 0 1200 508"><polygon points="0,0 655,0 502,508 0,508" fill="#1aa314"/></svg>
  <div class="surveil-photo" role="img" aria-label="Multi-sensor pan and tilt surveillance camera unit with two lens housings"></div>
  <h2>SURVEILLANCE CAMERAS SYSTEM</h2>
  <div class="rule" style="left:662px;top:121px;width:55px"></div>
  <p>The Orion is a revolutionary multi-sensor PTZ camera boasting a long-range 33X visible day/night camera, long-range thermal infrared zoom, and laser NIR illumination with LRF. This multi sensor payload enables the Orion to provide high-resolution imaging in virtually any environment from fog to complete darkness. Designed for accurate positioning of weapons systems, the pan/tilt unit meets and exceeds MIL-STD-810F military ratings for shock, vibration, temperature and dust/ water ingression.</p>
  <a class="btn-ghost">LEARN MORE</a>
</section>

<section class="overview">
  <h2>COMPANY OVERVIEW</h2>
  <div class="rule" style="left:112px;top:2706px;width:62px"></div>
  <p>A complete camera technical service company that installs, monitors, repairs, manage and maintain surveillance cameras for the government (military sources) and commercial clients. We provide our own team of highly skilled technicians for continuous consultation, training, and support. Technical Services: Surveillance camera installations, training and maintenance. Logistical Services: Supply management systems to include inventory, accountability, shipping, receiving and warehouse storage. Product Market camera systems, system software, network switches....</p>
  <div class="overview-diagram" role="img" aria-label="Hand-drawn diagram of three overlapping circles for mission, values and vision"></div>
</section>

<section class="partners">
  <h2 class="section-title" style="top:42px">OUR PARTNERS</h2>
  <div class="rule" style="left:565px;top:91px"></div>
  <svg class="abs" style="left:46px;top:140px" width="18" height="70" viewBox="0 0 18 70"><path d="M16 2L2 35l14 33" fill="none" stroke="#cfcfcf" stroke-width="2"/></svg>
  <svg class="abs" style="left:1138px;top:140px" width="18" height="70" viewBox="0 0 18 70"><path d="M2 2l14 33L2 68" fill="none" stroke="#cfcfcf" stroke-width="2"/></svg>
  <div class="logo-box" style="left:112px"><span></span></div>
  <div class="logo-box" style="left:311px"><span></span></div>
  <div class="logo-box" style="left:510px"><span></span></div>
  <div class="logo-box" style="left:708px"><span></span></div>
  <div class="logo-box" style="left:907px"><span></span></div>
</section>

<footer class="site-footer">
  <div class="footer-brand">Summit Field Solutions Group</div>
  <p class="footer-about">SFSG, LLC, We are a Self-certified Small Disabled Veteran Owned Business head quartered in Ridgefield, Georgia, the Home of our Field Team.</p>

  <div class="footer-col"><h4 style="left:423px">CONTACT INFO</h4></div>
  <ul class="footer-list contact-list">
    <li>Summit Field Solutions<br>Group, LLC (SFSG, LLC)</li>
    <li style="margin-top:26px">1420 Oakmere Road Ridgefield,<br>GA 30999</li>
    <li>Daniel Reyes +1 (555) 014-7730</li>
    <li>contact@pmwdtinc.com</li>
    <li>www.pmwdtinc.com</li>
  </ul>

  <div class="footer-col"><h4 style="left:742px">QUICK LINKS</h4></div>
  <ul class="footer-list links-list">
    <li>Home</li>
    <li>Company Overview</li>
    <li>Our Partners &amp; CLIENTS</li>
    <li>Who Are We</li>
    <li>Contact</li>
  </ul>

  <div class="footer-col"><h4 style="left:973px">FOLLOW US</h4></div>
  <div class="social" style="top:100px"><span class="ring"></span><div><small>Like us on</small><b>Facepage</b></div></div>
  <div class="social" style="top:158px"><span class="ring"></span><div><small>Follow us on</small><b>Chirper</b></div></div>
  <div class="social" style="top:216px"><span class="ring"></span><div><small>Follow us on</small><b>Linkwork</b></div></div>

  <div class="footer-rule"></div>
  <p class="copyright">© Copyright 2020 Pmwdtinc .All Rights Reserved</p>
</footer>

</body>
</html>
```